The Amber Tides (celtic rap album by Oskar Venlow)

Peace. I'm Oskar Venlow, I make celtic/druidic/pagan rap music. The album is called ' The Amber Tides ' which has to do with celtic cosmology: The Underworld (The Sea) is the realms of the past, the ancestors, trauma, transformation, knowledge of the old ways ... ; This World (The Land) is the realm of ordinary reality, our life, the present, skills, fertility ... ; and The Upperworld (The Sky) which is the realm of the gods, the future, goals, planning of harvest.... Three was a sacred number and describes the fullness of life and is symbolized by the triskele, e.g. found at Dunmorrow.

I have no idea for a cover lol, so go wild. It would be good if the three worlds are somehow featured.

This is one of the songs: https://www.clipvault-example.net/watch?v=qRtLmnWXpZA

Target Market(s)

pagans, spiritual people

Requirements
Must have
• something that references The Amber Tides (see description)
Nice to have
• Celtic symbol(s); contrasts between light and dark; past - present - future

```html
<!DOCTYPE html>
<html lang="en">
<head>
<meta charset="utf-8">
<title>The Amber Tides — Oskar Venlow</title>
<link rel="stylesheet" href="https://fonts.googleapis.com/css2?family=Allura&family=Montserrat:wght@500&family=Arimo&display=swap">
<style>
  :root {
    --backdrop: #e4e4e6;
    --night-deep: #16286a;
    --night-mid: #27449a;
    --night-glow: #3b5cb4;
    --dusk-violet: #6a5fa8;
    --dusk-rose: #d8b7b8;
    --sea-teal: #1f4a48;
    --sea-dark: #0f2a2c;
    --land-dark: #2a2a2e;
    --ink-light: #ffffff;
    --tag-black: #111111;
  }
  * { box-sizing: border-box; margin: 0; padding: 0; }
  html, body { width: 1200px; height: 1200px; overflow: hidden; }
  body {
    background: var(--backdrop);
    position: relative;
    font-family: "Arimo", Arial, sans-serif;
  }
  .cover {
    position: absolute;
    width: 720px;
    height: 720px;
    overflow: hidden;
  }
  .cover--back {
    left: 420px;
    top: 410px;
    background: radial-gradient(ellipse at 70% 20%, var(--night-glow) 0%, var(--night-mid) 45%, var(--night-deep) 100%);
  }
  .cover--front {
    left: 60px;
    top: 50px;
    box-shadow: 0 6px 18px rgba(0,0,0,0.35);
  }
  .cover-art {
    position: absolute;
    inset: 0;
    background:
      radial-gradient(circle at 82% 52%, rgba(255,225,205,0.95) 0%, rgba(232,190,190,0.6) 14%, rgba(150,120,180,0) 42%),
      linear-gradient(180deg, var(--night-mid) 0%, var(--dusk-violet) 35%, var(--dusk-rose) 52%, var(--land-dark) 66%, var(--sea-teal) 80%, var(--sea-dark) 100%);
  }
  .sky-art {
    position: absolute;
    inset: 0;
  }
  .album-title {
    position: absolute;
    font-family: "Allura", cursive;
    color: var(--ink-light);
    font-size: 60px;
    line-height: 0.95;
    font-weight: 400;
    white-space: nowrap;
  }
  .album-title span { display: block; }
  .album-title .second { padding-left: 70px; }
  .cover--front .album-title { right: 48px; top: 540px; }
  .cover--back .album-title { right: 70px; top: 535px; }
  .artist-tag {
    position: absolute;
    width: 30px;
    height: 150px;
    background: var(--tag-black);
    display: flex;
    align-items: center;
    justify-content: center;
  }
  .artist-tag span {
    transform: rotate(-90deg);
    white-space: nowrap;
    font-family: "Montserrat", sans-serif;
    font-weight: 500;
    font-size: 14px;
    letter-spacing: 0.5px;
    color: var(--ink-light);
  }
  .cover--front .artist-tag { left: 688px; top: 494px; }
  .cover--back .artist-tag { left: 666px; top: 530px; height: 160px; }
  .track-list {
    position: absolute;
    left: 70px;
    top: 362px;
    list-style: none;
    color: var(--ink-light);
    font-size: 16px;
  }
  .track-list li { height: 47px; }
  .track-list .num { display: inline-block; width: 20px; }
</style>
</head>
<body>
  <section class="cover cover--back" aria-label="Back cover">
    <div class="sky-art" role="img" aria-label="Starry night sky with a triskele of three spirals"></div>
    <ol class="track-list">
      <li><span class="num">6.</span> Sound track name</li>
      <li><span class="num">7.</span> Sound track name</li>
      <li><span class="num">8.</span> Sound track name</li>
      <li><span class="num">9.</span> Sound track name</li>
    </ol>
    <h2 class="album-title"><span>The Amber</span><span class="second">Tides</span></h2>
    <div class="artist-tag"><span>OSKAR VENLOW</span></div>
  </section>

  <section class="cover cover--front" aria-label="Front cover">
    <div class="cover-art" role="img" aria-label="Stone dolmen at dusk above crashing sea waves under a starry sky, overlaid with a faint triskele"></div>
    <h1 class="album-title"><span>The Amber</span><span class="second">Tides</span></h1>
    <div class="artist-tag"><span>OSKAR VENLOW</span></div>
  </section>
</body>
</html>
```